Morning Harvest Psalm Journal for the Weary Traveler on the Narrow Road

This is not an Eastern meditation method. No images or themes from guru style or Eastern meditations from Hinduism or Buddhism will work. This is a Biblical Christian-based method. Some sort of Divine Light from Heaven may be the look. Some "ancient scroll" for the title to be written in may work.

```html
<!DOCTYPE html>
<html lang="en">
<head>
<meta charset="utf-8">
<title>Morning Harvest – Psalm Journal</title>
<link href="https://fonts.googleapis.com/css2?family=Pirata+One&family=UnifrakturMaguntia&family=Great+Vibes&family=Tinos:wght@700&display=swap" rel="stylesheet">
<style>
  :root {
    --parchment-light: #c89a5c;
    --parchment-mid: #a97a42;
    --parchment-dark: #6e4722;
    --sky-glow: #fff4d6;
    --sky-orange: #f0a04a;
    --sky-rose: #b8707a;
    --rock: #b98350;
    --rock-shadow: #6a4126;
    --title-white: #ffffff;
    --title-shadow: #2b1a0f;
    --ink: #2a1a10;
  }
  * { margin: 0; padding: 0; box-sizing: border-box; }
  html, body { width: 849px; height: 1200px; overflow: hidden; background: var(--parchment-mid); }
  .cover {
    position: relative;
    width: 849px;
    height: 1200px;
    overflow: hidden;
    background:
      radial-gradient(ellipse at 50% 45%, rgba(230,190,120,0.35), transparent 70%),
      linear-gradient(180deg, var(--parchment-light) 0%, var(--parchment-mid) 60%, var(--parchment-dark) 100%);
  }
  .cover-scene {
    position: absolute;
    left: 0; top: 0;
    width: 849px; height: 780px;
    background:
      radial-gradient(circle at 110px 380px, var(--sky-glow) 0%, rgba(255,220,150,0.9) 12%, rgba(240,160,74,0.5) 28%, transparent 45%),
      radial-gradient(ellipse at 620px 300px, var(--rock) 0%, #a06a3c 35%, var(--rock-shadow) 70%, transparent 85%),
      linear-gradient(180deg, var(--sky-rose) 0%, var(--sky-orange) 30%, #c98a52 55%, #b48250 80%);
    -webkit-mask-image: linear-gradient(180deg, #000 65%, transparent 100%);
    mask-image: linear-gradient(180deg, #000 65%, transparent 100%);
  }
  .title {
    position: absolute;
    left: 0; width: 100%;
    text-align: center;
    font-family: "Pirata One", fantasy;
    color: var(--title-white);
    text-shadow: 4px 6px 0 var(--title-shadow), 0 0 18px rgba(0,0,0,0.35);
    line-height: 1;
  }
  .title-line-one { top: 500px; font-size: 138px; letter-spacing: 2px; }
  .title-line-two { top: 668px; font-size: 172px; letter-spacing: 3px; }
  .subtitle {
    position: absolute;
    top: 888px; left: 0; width: 100%;
    text-align: center;
    font-family: "UnifrakturMaguntia", serif;
    font-size: 68px;
    color: var(--ink);
    line-height: 1;
  }
  .tagline {
    position: absolute;
    top: 985px; left: 0; width: 100%;
    text-align: center;
    font-family: "Great Vibes", cursive;
    font-size: 50px;
    color: var(--ink);
    line-height: 1.1;
  }
  .author {
    position: absolute;
    top: 1118px; left: 0; width: 100%;
    text-align: center;
    font-family: "Tinos", serif;
    font-weight: 700;
    font-size: 44px;
    color: var(--ink);
  }
</style>
</head>
<body>
  <main class="cover">
    <div class="cover-scene" role="img" aria-label="Sunrise over three crosses on a distant hill, seen from inside an open rock tomb with folded linen cloth on a stone ledge"></div>
    <h1>
      <span class="title title-line-one">MORNING</span>
      <span class="title title-line-two">HARVEST</span>
    </h1>
    <p class="subtitle">Psalm Journal</p>
    <p class="tagline">For the Weary Traveler on the Narrow Road</p>
    <p class="author">Samuel Whitaker</p>
  </main>
</body>
</html>
```